Letterhead & Email Signature Design

Kindly assist redesign this letterhead as well as the Email signature. I have uploaded the current designs that needs some new look

```html
<!DOCTYPE html>
<html lang="en">
<head>
<meta charset="utf-8">
<title>Tlhako Rammala Inc. – Letterhead &amp; Email Signature</title>
<link rel="stylesheet" href="https://fonts.googleapis.com/css2?family=Lato:wght@400;700&family=Montserrat:wght@800&display=swap">
<style>
  :root {
    --ink-dark: #3a3a3c;
    --brand-blue: #1769a5;
    --paper: #ffffff;
    --frame: #9a9a9a;
  }
  * { margin: 0; padding: 0; box-sizing: border-box; }
  html, body { width: 713px; height: 1200px; overflow: hidden; background: var(--paper); }
  body { position: relative; font-family: 'Lato', sans-serif; color: var(--paper); }

  .letterhead-sheet {
    position: absolute; left: 37.5px; top: 32.7px; width: 638px; height: 902px;
    border: 0.6px solid var(--frame); background: var(--paper);
  }
  .letterhead-header {
    position: absolute; left: 83px; top: 79px; width: 546px; height: 157px;
  }
  .letterhead-header .band { position: absolute; inset: 0; }
  .emblem {
    position: absolute; background: var(--paper); border-radius: 50%;
    display: flex; align-items: center; justify-content: center;
    color: var(--ink-dark); font-family: 'Lato', sans-serif; font-weight: 400;
    font-size: 13px; letter-spacing: 0.2px;
  }
  .letterhead-header .emblem { left: 41px; top: 15.5px; width: 112px; height: 99px; }
  .practice-areas {
    position: absolute; left: 0; width: 194px; top: 122px; text-align: center;
    font-size: 7.2px; font-weight: 700; letter-spacing: 0.1px;
  }
  .reg-number {
    position: absolute; left: 0; width: 194px; top: 133px; text-align: center;
    font-size: 5.8px; letter-spacing: 0.2px;
  }
  .firm-name {
    font-family: 'Montserrat', sans-serif; font-weight: 800; letter-spacing: 0.4px;
  }
  .letterhead-header .firm-name {
    position: absolute; right: 16px; top: 48px; font-size: 18.5px;
  }
  .contact-line {
    position: absolute; right: 16px; display: flex; align-items: center; gap: 6px;
    font-size: 9.6px; font-weight: 700; letter-spacing: 0.4px;
  }
  .contact-line svg { width: 12px; height: 12px; }
  .contact-line.phone { top: 73px; }
  .contact-line.fax { top: 87px; }
  .contact-email {
    position: absolute; right: 16px; top: 101px; font-size: 9px; letter-spacing: 0.3px;
  }
  .contact-address {
    position: absolute; right: 16px; top: 120px; text-align: right;
    font-size: 9px; line-height: 10.6px; letter-spacing: 0.2px;
  }
  .letterhead-footer {
    position: absolute; left: 83px; top: 872px; width: 546px; height: 17.5px;
    background: var(--ink-dark); display: flex; align-items: center;
    justify-content: space-between; padding: 0 10px 0 9px; font-size: 9.2px;
    letter-spacing: 0.2px;
  }
  .letterhead-footer .label { font-size: 7px; }

  .email-signature {
    position: absolute; left: 94px; top: 988px; width: 529px; height: 173px;
    display: flex;
  }
  .signature-identity {
    position: relative; width: 202.5px; height: 100%; background: var(--ink-dark);
  }
  .signature-identity .emblem { left: 47px; top: 28.5px; width: 112px; height: 99px; }
  .signature-director {
    position: absolute; left: 0; width: 208px; top: 134px; text-align: center;
    font-size: 7.5px; letter-spacing: 0.2px;
  }
  .signature-director strong { font-size: 9px; font-weight: 700; }
  .signature-established {
    position: absolute; left: 0; width: 208px; top: 145.5px; text-align: center;
    font-size: 7.8px; font-weight: 700; letter-spacing: 0.5px;
  }
  .signature-details {
    position: relative; flex: 1; background: var(--brand-blue);
  }
  .signature-details .firm-name {
    position: absolute; left: 25.5px; top: 31px; font-size: 18px;
  }
  .detail-row {
    position: absolute; left: 27px; display: flex; align-items: flex-start; gap: 7px;
    font-size: 9.2px; letter-spacing: 0.3px; line-height: 11px;
  }
  .detail-row svg { width: 12px; height: 12px; flex: none; margin-top: -0.5px; }
  .detail-row.bold { font-weight: 700; }
  .detail-row.phone { top: 62px; }
  .detail-row.email { top: 80px; }
  .detail-row.web { top: 91px; }
  .detail-row.office-main { top: 109px; }
  .detail-row.office-branch { top: 136px; }
</style>
</head>
<body>

<section class="letterhead-sheet" aria-label="Letterhead"></section>

<header class="letterhead-header">
  <svg class="band" viewBox="0 0 546 157" preserveAspectRatio="none" aria-hidden="true">
    <rect width="546" height="157" fill="var(--brand-blue)"/>
    <polygon points="0,0 273.5,0 200.5,157 0,157" fill="var(--ink-dark)"/>
  </svg>
  <div class="emblem">Tlhako Rammala</div>
  <p class="practice-areas">ATTORNEYS | CONVEYANCERS | NOTARIES</p>
  <p class="reg-number">Reg. No.: 2009/004812/21</p>

  <h1 class="firm-name">TLHAKO RAMMALA INC.</h1>
  <p class="contact-line phone">
    <svg viewBox="0 0 24 24" aria-hidden="true"><circle cx="12" cy="12" r="10.5" fill="none" stroke="currentColor" stroke-width="1.8"/><path d="M8 6.5l2 .2 1 3-1.4 1.2a7 7 0 0 0 3.5 3.5l1.2-1.4 3 1 .2 2c-.3.8-1.2 1.3-2 1.2A10 10 0 0 1 6.8 8.5c-.1-.8.4-1.7 1.2-2z" fill="currentColor"/></svg>
    012 450 3318
  </p>
  <p class="contact-line fax">
    <svg viewBox="0 0 24 24" aria-hidden="true"><rect x="6" y="2" width="12" height="6" fill="currentColor"/><rect x="2" y="9" width="20" height="9" rx="2" fill="currentColor"/><rect x="6" y="14" width="12" height="8" fill="var(--brand-blue)" stroke="currentColor" stroke-width="1.8"/><path d="M8.5 17h7M8.5 19.5h7" stroke="currentColor" stroke-width="1.2"/></svg>
    012 450 3319
  </p>
  <p class="contact-email">info@tlhakorammala.co.za</p>
  <p class="contact-address">Acacia Office Park, First Floor,<br>Block C, 214 Kingfisher Road, Lynnwood, 0042</p>
</header>

<footer class="letterhead-footer">
  <p><span class="label">Directors:</span> T P Nkadimeng B.PROC LLB (Hons) | R Rammala (LLB)</p>
  <p><span class="label">Consultant:</span> LM Rammala</p>
</footer>

<section class="email-signature" aria-label="Email signature">
  <div class="signature-identity">
    <div class="emblem">Tlhako Rammala</div>
    <p class="signature-director">Director: <strong>T P Nkadimeng B.PROC LLB</strong></p>
    <p class="signature-established">-Est. 2009-</p>
  </div>
  <div class="signature-details">
    <h2 class="firm-name">TLHAKO RAMMALA INC.</h2>
    <p class="detail-row bold phone">
      <svg viewBox="0 0 24 24" aria-hidden="true"><path d="M6 3l3 .3 1.5 4.2-2 1.7a10 10 0 0 0 5 5l1.7-2 4.2 1.5.3 3c-.4 1.2-1.7 2-3 1.8A15 15 0 0 1 4.2 6C4 4.7 4.8 3.4 6 3z" fill="none" stroke="currentColor" stroke-width="1.8"/><path d="M14 3a7 7 0 0 1 7 7M14 7a3 3 0 0 1 3 3" fill="none" stroke="currentColor" stroke-width="1.6"/></svg>
      +27 12 450 3318
    </p>
    <p class="detail-row bold email">
      <svg viewBox="0 0 24 24" aria-hidden="true"><rect x="2" y="5" width="20" height="14" fill="none" stroke="currentColor" stroke-width="1.8"/><path d="M2 5l10 8 10-8M2 19l7.5-7M22 19l-7.5-7" fill="none" stroke="currentColor" stroke-width="1.6"/></svg>
      lerato@tlhakorammala.co.za
    </p>
    <p class="detail-row bold web">
      <svg viewBox="0 0 24 24" aria-hidden="true"><circle cx="12" cy="12" r="10" fill="none" stroke="currentColor" stroke-width="1.8"/><ellipse cx="12" cy="12" rx="4.5" ry="10" fill="none" stroke="currentColor" stroke-width="1.4"/><path d="M2 12h20M4 7h16M4 17h16" stroke="currentColor" stroke-width="1.4"/></svg>
      www.tlhakorammalainc.co.za
    </p>
    <p class="detail-row office-main">
      <svg viewBox="0 0 24 24" aria-hidden="true"><path d="M12 2a6 6 0 0 1 6 6c0 4.5-6 11-6 11S6 12.5 6 8a6 6 0 0 1 6-6z" fill="none" stroke="currentColor" stroke-width="1.8"/><circle cx="12" cy="8" r="2.2" fill="currentColor"/><path d="M8 18.5c-3 .5-5 1.4-5 2.3C3 22 7 23 12 23s9-1 9-2.2c0-.9-2-1.8-5-2.3" fill="none" stroke="currentColor" stroke-width="1.4"/></svg>
      <span>214 Kingfisher Road,<br>Acacia Office Park, First Floor, Block C.</span>
    </p>
    <p class="detail-row office-branch">
      <svg viewBox="0 0 24 24" aria-hidden="true"><path d="M12 2a6 6 0 0 1 6 6c0 4.5-6 11-6 11S6 12.5 6 8a6 6 0 0 1 6-6z" fill="none" stroke="currentColor" stroke-width="1.8"/><circle cx="12" cy="8" r="2.2" fill="currentColor"/><path d="M8 18.5c-3 .5-5 1.4-5 2.3C3 22 7 23 12 23s9-1 9-2.2c0-.9-2-1.8-5-2.3" fill="none" stroke="currentColor" stroke-width="1.4"/></svg>
      48 Marula Street, Westenburg, Polokwane.
    </p>
  </div>
</section>

</body>
</html>
```